依頼詳細
ホームページのロゴを使いたいです。デリケートな問題ですが、事前に考え、ぜひ終活のお話をきき、
エンディングノートを一緒に書きたくなるような内容。H25年11月、9,10日の産業祭や、ポスティングで使います。
ですが、そこから繋がりができ、御葬儀の依頼をふやしたいです。
終活のイメージは、ホームページのブログの手と手を繋ぐ絵でお願したいです。
記載項目
あおば典礼(ロゴ) キャッチコピー 『大切な人を見送る方々とともに・・・まごころをこめて・・・』
〒317-0088 茨城県日立市緑苑町8-27-3
電話0294-58-7261 FAX0294-43-3540
ホームページ、あおば典礼 検索 フェイスブックページ
御葬儀の内容、金額等
終活相談会の実施、個別、グループで依頼、場所は御自宅、集会所、あおば典礼事務所でも定期的に実施しています。(ホームページ内ブログ、フェイスブックページ、事務所外掲示板、お電話にてご確認下さい。
サイズ
A4
ページ数
両面
希望イメージ
シンプル 複雑
単色 カラフル
暗い 明るい
日常 高級
遊び心 厳粛
未来的 伝統的
女性的 男性的
希望する色
紫、ピンク、
納品ファイル
• 高解像度JPG (.jpg)
補足説明
あおば典礼のホームページ参考にして下さい。
お世話になります。
終活と、御葬儀の宣伝も入れて下さい。

toriyoshiさんの提案は、お葬儀の事と、終活のこと、会社の売り、私どもの気持ちを汲んだ内容が、よくホームページやファイルを読み込んでくれていたと思いました。

お世話になりました。
初めての依頼で要領が分からず、提案しずらかったと思います。
沢山の提案をいただき、自分達が気づかなかった会社の特徴も分かりました。
lanternflyさんには、質問していただいた内容に、すぐに対応して
修正した提案をあげてもらい、ありがたい気持ちです。
会員様へ送っている、瓦版でしたらlanternflyさんの提案が親近感あってよかったと思います。皆さん、きれいに仕上げてくださり ありがとうございました。
また、何か機会がありましたら その時は宜しくお願い申しあげます。

```html
<!DOCTYPE html>
<html lang="ja">
<head>
<meta charset="utf-8">
<title>あおば典礼 終活のご案内</title>
<link rel="stylesheet" href="https://fonts.googleapis.com/css2?family=Kosugi+Maru&family=Noto+Serif+JP:wght@500;700&display=swap">
<style>
:root{
  --pink-deep:#e0407a;
  --pink:#f08fb0;
  --pink-soft:#fbd3e0;
  --pink-pale:#fdeaf0;
  --red:#d8102a;
  --ink:#3a2a2e;
  --blue:#3c5fb5;
  --white:#ffffff;
}
*{margin:0;padding:0;box-sizing:border-box}
html,body{width:849px;height:1200px;overflow:hidden}
body{font-family:"Kosugi Maru",sans-serif;color:var(--ink);
  background:linear-gradient(180deg,var(--white) 0%,var(--pink-pale) 30%,var(--pink-soft) 100%)}
.poster{position:relative;width:849px;height:1200px}
.abs{position:absolute}
.brand{display:flex;align-items:center;gap:12px;font-family:"Noto Serif JP",serif;font-weight:700;color:var(--pink-deep)}
.brand-dot{width:34px;height:34px;border-radius:50%;background:var(--pink-deep)}
.brand-top{left:0;right:0;top:14px;height:50px;justify-content:center;font-size:40px;letter-spacing:6px}
.catch{left:0;right:0;top:72px;text-align:center;font-family:"Noto Serif JP",serif;font-weight:700;font-size:22px}
.catch em{font-style:normal;color:var(--red);font-size:26px}
.question{left:0;right:0;top:108px;text-align:center;font-family:"Noto Serif JP",serif;font-size:18px;font-weight:500}
.definition{left:262px;top:140px;width:326px;padding:12px 16px;background:var(--pink);color:var(--white);font-size:13px;line-height:1.7;border-radius:4px}
.message{left:108px;top:242px;width:640px;font-size:14.5px;line-height:2.05}
.message .hl{color:var(--red)}
.arc{left:252px;top:370px;overflow:visible}
.hands{left:295px;top:440px;width:254px;height:254px;border-radius:50%;
  background:radial-gradient(circle,var(--pink-soft) 0%,#f6b9cc 55%,#e9a2ba 100%)}
.services{left:30px;top:552px;font-size:14px;line-height:1.9;color:var(--red);font-weight:bold;list-style:none}
.services li::before{content:"◆";margin-right:4px}
.services .note{color:var(--ink);font-weight:normal}
.free{left:612px;top:500px;width:210px;text-align:center;color:var(--red);font-size:19px;line-height:1.55}
.pill{left:28px;top:702px;padding:6px 16px;background:var(--pink-deep);color:var(--white);font-size:15px;border-radius:18px}
.more{left:40px;top:746px;display:flex;align-items:center;gap:8px;font-size:15px;font-weight:bold}
.more-arrow{width:22px;height:22px;border-radius:50%;background:var(--pink-deep);color:var(--white);font-size:13px;display:flex;align-items:center;justify-content:center}
.support{left:625px;top:690px;width:200px;font-size:13px;line-height:1.7}
.club{left:28px;top:806px;width:212px;height:128px;background:var(--white);border:2px solid var(--pink);padding:10px 12px;font-size:12.5px;line-height:1.7}
.club h3{font-size:15px;color:var(--pink-deep);margin-bottom:4px}
.card{left:255px;top:850px;width:155px;height:126px;border-radius:8px;background:linear-gradient(135deg,var(--pink-soft),#c46a98)}
.contact{left:425px;top:806px;width:398px;height:170px;background:var(--white);border:2px solid var(--pink);padding:10px 14px;font-size:13px;line-height:1.6}
.contact .alert{color:var(--red)}
.brand-foot{right:40px;top:932px;font-size:20px;letter-spacing:2px}
.brand-foot .brand-dot{width:22px;height:22px}
</style>
</head>
<body>
<div class="poster">
  <div class="abs brand brand-top"><span class="brand-dot"></span>あおば典礼</div>
  <p class="abs catch">「大切な人を見送る方々とともに…<em>まごころをこめて</em>…」</p>
  <p class="abs question">みなさまは、終活という言葉をご存知でしょうか？</p>
  <p class="abs definition">終活とは、愛する人・大切な人へ、そして自分のために、「ありがとう」の気持ちを伝える準備であると私たちは考えています。</p>
  <div class="abs message">
    <p>私どもは、人生の締めくくりを自分らしいものにしていただため、</p>
    <p class="hl">ご自身の想いを綴るエンディングノートに記すお手伝いから、</p>
    <p class="hl">ご葬儀の執行い、法事…と、継続したお手伝いをさせていただいております。</p>
    <p>みなさまのご質問・ご要望に応えるため、各種の専門家と提携も組んでおります。</p>
  </div>
  <svg class="abs arc" width="340" height="100" viewBox="0 0 340 100">
    <defs><path id="arcPath" d="M25 95 A200 200 0 0 1 315 95"/></defs>
    <text fill="var(--blue)" font-size="19" font-family="Kosugi Maru, sans-serif"><textPath href="#arcPath" startOffset="50%" text-anchor="middle">様々なご相談にお応えいたします</textPath></text>
  </svg>
  <div class="abs hands" role="img" aria-label="花を中心に人々が手をつなぐ輪のイラスト"></div>
  <ul class="abs services">
    <li>相続・遺言書等の法的相談</li>
    <li>お葬式に関すること</li>
    <li>宗派による儀式の質問</li>
    <li>散骨等の埋葬に関する事</li>
    <li class="note">お気軽にご相談ください！</li>
  </ul>
  <p class="abs free">ご葬儀についての<br>ご相談やお見積りは<br>無料＆年中無休</p>
  <p class="abs pill">あおば典礼ってどんなところ？</p>
  <p class="abs more"><span class="more-arrow">▶</span>くわしくは裏面へ</p>
  <p class="abs support">みなさまが安心して終活を迎えられるよう、全力でサポートしております。</p>
  <div class="abs club">
    <h3>あおば典礼 友の会</h3>
    <p>『友の会』会員様専用。入会金1,000円の永年会員、年会費・更新費は一切不要です。</p>
  </div>
  <div class="abs card" role="img" aria-label="友の会の会員カードの写真"></div>
  <div class="abs contact">
    <p>〒317-0088<br>茨城県日立市緑苑町8-27-3</p>
    <p>電話：0294-58-7261</p>
    <p>FAX：0294-58-7269</p>
    <p>HP　http://www.aobatenrei-hitachi.jp</p>
    <p>ブログ　http://aobatenrei-diary.jp/</p>
    <p class="alert">お気軽にお問い合わせ下さい!!</p>
  </div>
  <div class="abs brand brand-foot"><span class="brand-dot"></span>あおば典礼</div>
</div>
</body>
</html>
```